Product Sales Website Design - E-commerce - Shopify etc

We have been selling printing equipment for some time now and think that it will be useful to sell the products on the internet, using a simple e-commerce platform, such as shopify etc. There are roughly a few dozen products - so basically, the idea is to have a modern, simple and clean home page. When someone looks at it, they think, this is it - I want to buy here. I am not going to impose any ideas or say how I want it done.

Just so you know, at the moment there are three categories of products. One being printers, scanners and accessories.

I am excited by this whole project and don't want to have good designers backing out because they feel i am imposing restrictions. Feel free to impress me.

Industry/Entity Type

E-Commerce

Requirements
Must have
• integration with an e-commerce platform is a must or show how to integrate, so I can easily introduce further products.

```html
<!DOCTYPE html>
<html lang="en">
<head>
<meta charset="utf-8">
<title>PrintWorks – Printers, Scanners and Accessories</title>
<link href="https://fonts.googleapis.com/css2?family=Exo+2:ital,wght@1,700;1,800&family=PT+Sans:wght@400;700&display=swap" rel="stylesheet">
<style>
  :root {
    --backdrop: #6b6b6b;
    --ink: #333333;
    --charcoal: #3a3a3a;
    --topbar: #353535;
    --lime: #d3de22;
    --lime-soft: #e4eb8a;
    --white: #ffffff;
    --muted: #cfcfcf;
    --price-bg: #e9e9e9;
  }
  * { box-sizing: border-box; margin: 0; padding: 0; }
  html, body {
    width: 1200px; height: 896px; overflow: hidden;
    background: var(--backdrop);
    font-family: "PT Sans", Arial, sans-serif;
  }
  .page {
    position: absolute; left: 208px; top: 14px;
    width: 786px; height: 882px;
    background: var(--white);
    border: 2px solid #222;
    border-bottom: none;
    overflow: hidden;
  }
  /* top utility bar */
  .utility-bar {
    height: 42px; background: var(--topbar);
    display: flex; align-items: center; justify-content: flex-end;
    padding-right: 46px; gap: 30px;
  }
  .utility-bar a { color: var(--white); font-size: 13px; font-weight: 700; text-decoration: none; }
  .utility-bar .cart { margin-left: 30px; width: 26px; height: 22px; }

  /* main navigation */
  .main-nav {
    height: 57px; background: var(--lime);
    border-top: 2px solid var(--white);
    border-bottom: 2px solid var(--ink);
    display: flex; align-items: center;
    padding: 0 30px 0 16px;
  }
  .brand { font-size: 21px; font-weight: 700; color: var(--ink); }
  .main-nav ul { list-style: none; display: flex; margin-left: auto; gap: 0; }
  .main-nav li a {
    display: block; font-size: 17px; font-weight: 700; color: var(--ink);
    text-decoration: none; margin-left: 66px; padding-top: 6px;
  }
  .main-nav li:first-child a { margin-left: 0; }
  .search-icon { width: 18px; height: 18px; margin-left: 40px; margin-top: 2px; }

  /* hero */
  .hero { position: relative; height: 352px; border-bottom: 2px solid var(--lime-soft); }
  .hero-photo {
    position: absolute; left: 53px; top: 78px; width: 304px; height: 176px;
    background: linear-gradient(160deg, #4a4a4a 0%, #1c1c1c 55%, #8fb3d9 100%);
    border-radius: 8px;
  }
  .hero-title {
    position: absolute; right: 96px; top: 42px; text-align: right;
    font-family: "Exo 2", Arial, sans-serif; font-style: italic; font-weight: 700;
    font-size: 38px; line-height: 1.2; color: var(--charcoal);
  }
  .shop-now {
    position: absolute; left: 508px; top: 161px; width: 142px; height: 53px;
    background: var(--charcoal); color: var(--white); border-radius: 9px;
    font-family: "Exo 2", Arial, sans-serif; font-style: italic; font-weight: 800;
    font-size: 21px; display: flex; align-items: center; justify-content: center;
    text-decoration: none;
  }
  .slide-dots {
    position: absolute; left: 312px; top: 314px; display: flex; gap: 5px;
  }
  .slide-dots span { width: 17px; height: 17px; border-radius: 50%; background: var(--charcoal); }
  .slide-dots span.active { background: var(--lime); }

  /* popular products */
  .popular { position: relative; height: 319px; }
  .section-title {
    position: absolute; left: 20px; top: 14px;
    font-family: "Exo 2", Arial, sans-serif; font-style: italic; font-weight: 700;
    font-size: 24px; color: var(--charcoal);
  }
  .carousel-arrow { position: absolute; top: 124px; width: 44px; height: 44px; }
  .carousel-arrow.prev { left: 40px; }
  .carousel-arrow.next { left: 702px; }
  .product-card {
    position: absolute; top: 63px; width: 175px; height: 212px;
    border: 2px solid var(--lime-soft); background: var(--white);
    padding: 12px 8px 0;
  }
  .product-card:nth-of-type(1) { left: 102px; }
  .product-card:nth-of-type(2) { left: 306px; }
  .product-card:nth-of-type(3) { left: 504px; }
  .product-photo { height: 120px; background: #f1f1f1; }
  .product-photo.printer { background: linear-gradient(150deg, #e8e8e8, #2a2a2a 60%, #7aa3c9); }
  .product-photo.ink { background: linear-gradient(90deg, #2d2d2d, #d2337d 35%, #2f7fd0 60%, #f2e23a 85%); }
  .product-photo.scanner { background: linear-gradient(150deg, #f5f5f5, #3a3a3a 60%, #9a9a9a); }
  .product-name {
    height: 33px; background: var(--lime); color: var(--ink);
    font-size: 11px; font-weight: 700; display: flex; align-items: center; justify-content: center;
  }
  .product-buy { display: flex; height: 30px; }
  .price {
    flex: 1; background: var(--price-bg); font-size: 10px; font-weight: 700; color: var(--ink);
    display: flex; align-items: center; justify-content: center;
  }
  .add-to-cart {
    flex: 1; background: var(--charcoal); color: var(--white); font-size: 10px; font-weight: 700;
    display: flex; align-items: center; justify-content: center; text-decoration: none;
  }

  /* footer */
  .site-footer { position: relative; height: 165px; background: var(--charcoal); color: var(--white); }
  .footer-links { position: absolute; left: 20px; top: 10px; display: flex; gap: 22px; list-style: none; }
  .footer-links a { color: var(--white); text-decoration: none; font-size: 16px; font-weight: 700; }
  .footer-brand { position: absolute; right: 56px; top: 12px; font-size: 18px; font-weight: 700; }
  .social { position: absolute; right: 20px; top: 63px; display: flex; gap: 4px; }
  .social span { width: 14px; height: 14px; background: var(--white); border-radius: 2px; }
  .copyright { position: absolute; left: 0; right: 0; top: 92px; text-align: center; font-size: 11px; font-weight: 700; }
</style>
</head>
<body>
<div class="page">
  <div class="utility-bar">
    <a href="#">About us</a>
    <a href="#">Contact us</a>
    <svg class="cart" viewBox="0 0 26 22" aria-label="Cart">
      <path d="M1 2h4l3 11h13l3-8H7" fill="none" stroke="#fff" stroke-width="2.4" stroke-linejoin="round"/>
      <rect x="8" y="6" width="14" height="6" fill="#fff"/>
      <circle cx="10" cy="18" r="2.2" fill="#fff"/>
      <circle cx="19" cy="18" r="2.2" fill="#fff"/>
    </svg>
  </div>

  <nav class="main-nav">
    <span class="brand">PrintWorks</span>
    <ul>
      <li><a href="#">Printers</a></li>
      <li><a href="#">Scanners</a></li>
      <li><a href="#">Accessories</a></li>
    </ul>
    <svg class="search-icon" viewBox="0 0 18 18" aria-label="Search">
      <circle cx="7" cy="7" r="4.8" fill="none" stroke="#333" stroke-width="2.6"/>
      <path d="M10.5 10.5l5.5 5.5" stroke="#333" stroke-width="3" stroke-linecap="round"/>
    </svg>
  </nav>

  <section class="hero">
    <div class="hero-photo" role="img" aria-label="Photo of a black inkjet printer printing a colour photo"></div>
    <h1 class="hero-title">Save up to 22%<br>Printer sale</h1>
    <a class="shop-now" href="#">Shop now</a>
    <div class="slide-dots"><span class="active"></span><span></span><span></span><span></span><span></span></div>
  </section>

  <section class="popular">
    <h2 class="section-title">Popular products</h2>
    <svg class="carousel-arrow prev" viewBox="0 0 44 44" aria-label="Previous">
      <circle cx="22" cy="22" r="21" fill="#3a3a3a"/>
      <path d="M25 13l-9 9 9 9" fill="none" stroke="#fff" stroke-width="4.5" stroke-linecap="round" stroke-linejoin="round"/>
    </svg>
    <article class="product-card">
      <div class="product-photo printer" role="img" aria-label="Photo of a photo printer"></div>
      <div class="product-name">Lumora Photo Pro</div>
      <div class="product-buy"><span class="price">$169.99</span><a class="add-to-cart" href="#">Add to cart</a></div>
    </article>
    <article class="product-card">
      <div class="product-photo ink" role="img" aria-label="Photo of four colour ink cartridges"></div>
      <div class="product-name">Inkwell Color Cartridge</div>
      <div class="product-buy"><span class="price">$99.99</span><a class="add-to-cart" href="#">Add to cart</a></div>
    </article>
    <article class="product-card">
      <div class="product-photo scanner" role="img" aria-label="Photo of a flatbed scanner with open lid"></div>
      <div class="product-name">Lumora Photo Pro</div>
      <div class="product-buy"><span class="price">$169.99</span><a class="add-to-cart" href="#">Add to cart</a></div>
    </article>
    <svg class="carousel-arrow next" viewBox="0 0 44 44" aria-label="Next">
      <circle cx="22" cy="22" r="21" fill="#3a3a3a"/>
      <path d="M19 13l9 9-9 9" fill="none" stroke="#fff" stroke-width="4.5" stroke-linecap="round" stroke-linejoin="round"/>
    </svg>
  </section>

  <footer class="site-footer">
    <ul class="footer-links">
      <li><a href="#">Products</a></li>
      <li><a href="#">About us</a></li>
      <li><a href="#">Contact us</a></li>
    </ul>
    <span class="footer-brand">PrintWorks</span>
    <div class="social"><span></span><span></span></div>
    <p class="copyright">Copyright 2014</p>
  </footer>
</div>
</body>
</html>
```